Sign Up Page Design

We wish to revamp the sign up page of our real estate website (www.trellisparcelmarket.com) in order to improve conversion rate. This sign up page has two steps, thus you should come up with 2 pages of sample. We are more interested in getting a design created by a UX designer who has already created other sign up pages and knows the mind of an online buyer. We are sending attached the screenshot of the current sign up page for you to take as basis. Feel free to improve them and come up with something better which can help increase conversion rate.
Updates

We have changed the project settings to NON REFUNDABLE.... so please keep sending your designs. We look forward for your creativity!!!

Industry/Entity Type

Real Estate

```html
<!DOCTYPE html>
<html lang="en">
<head>
<meta charset="utf-8">
<title>Trellis Parcel Market – Sign Up</title>
<link href="https://fonts.googleapis.com/css2?family=Arimo:ital,wght@0,400;0,700;1,400&family=Carlito:wght@400;700&display=swap" rel="stylesheet">
<style>
:root{
  --header-top:#d2d2d2;
  --header-bottom:#bdbdbd;
  --hero-bg:#e5e5e5;
  --page-bg:#f7f7f7;
  --panel-bg:#efefef;
  --brand-blue:#2a6fae;
  --brand-green:#6a9f3a;
  --accent-orange:#f58220;
  --selected-orange:#c0522a;
  --text-dark:#1d1d1d;
  --text-mid:#555;
  --text-soft:#888;
  --field-bg:#fff;
  --btn-blue:#2d6ba3;
  --btn-orange:#ff8a00;
  --btn-green:#8cc152;
  --btn-black:#222;
}
*{margin:0;padding:0;box-sizing:border-box}
html,body{width:1200px;height:899px;overflow:hidden}
body{position:relative;background:var(--page-bg);font-family:"Arimo",Arial,sans-serif;color:var(--text-dark)}
.site-header{position:absolute;left:0;top:0;width:1200px;height:76px;background:linear-gradient(var(--header-top),var(--header-bottom));border-bottom:2px solid #cfcfcf}
.brand{position:absolute;left:0;width:1200px;top:22px;display:flex;justify-content:center;align-items:center;gap:10px}
.brand-mark{width:26px;height:26px;background:var(--brand-green)}
.brand-name{font-family:"Carlito",Calibri,sans-serif;font-weight:700;font-size:25px;color:var(--brand-blue)}
.hero{position:absolute;left:0;top:78px;width:1200px;height:273px;background:var(--hero-bg)}
.hero-title{position:absolute;top:116px;width:1200px;text-align:center;font-family:"Carlito",Calibri,sans-serif;font-weight:700;font-size:21px;color:var(--brand-blue)}
.hero-sub{position:absolute;top:147px;width:1200px;text-align:center;font-weight:700;font-size:13px}
.hero-quote{position:absolute;left:262px;top:200px;width:766px;text-align:center;font-style:italic;font-size:13.5px;line-height:20px;color:#444}
.category{position:absolute;text-align:center;font-weight:700;font-size:13px;color:var(--text-mid)}
.category .thumb{display:block;border:3px solid #fff;box-shadow:0 0 2px #999;margin-bottom:8px}
.category.is-selected{color:var(--selected-orange)}
.category.is-selected .thumb{border-color:var(--selected-orange);margin-bottom:6px}
.selected-pointer{position:absolute;left:414px;top:300px;width:0;height:0;border-left:8px solid transparent;border-right:8px solid transparent;border-bottom:9px solid var(--selected-orange)}
.access-panel{position:absolute;left:78px;top:465px;width:1043px;height:363px;background:var(--panel-bg)}
.access-title{position:absolute;left:160px;top:492px;font-family:"Carlito",Calibri,sans-serif;font-weight:700;font-size:34px;color:#666;letter-spacing:.5px}
.access-title span{color:var(--accent-orange);font-size:30px}
.access-arrow{position:absolute;left:100px;top:516px}
.benefit{position:absolute;left:159px;width:406px;height:46px;border-radius:6px;border:1px solid #333;display:flex;align-items:center;justify-content:center;font-weight:700;font-size:14.5px;color:#fff;text-shadow:0 1px 1px rgba(0,0,0,.5)}
.benefit.blue{top:569px;background:linear-gradient(#3e80ba,var(--btn-blue))}
.benefit.orange{top:626px;background:linear-gradient(#ffa531,var(--btn-orange))}
.benefit.green{top:686px;background:linear-gradient(#a7d46f,var(--btn-green))}
.benefit.black{top:744px;background:linear-gradient(#444,var(--btn-black))}
.register-box{position:absolute;left:629px;top:489px;width:458px;height:314px;border:1px solid #aaa;background:#e9e9e9}
.register-title{position:absolute;left:659px;top:496px;font-family:"Carlito",Calibri,sans-serif;font-weight:700;font-size:26px;color:#666;letter-spacing:.5px}
.register-title span{color:var(--brand-green)}
.register-sub{position:absolute;left:692px;top:530px;font-family:"Carlito",Calibri,sans-serif;font-size:18px;color:var(--brand-green)}
.keys-art{position:absolute;left:1015px;top:465px;width:86px;height:125px;border-radius:40px 40px 10px 10px;background:linear-gradient(160deg,#c9c9c9,#8a8a8a 60%,#b59a4a)}
.field{position:absolute;left:642px;width:415px;height:35px;background:var(--field-bg);border-radius:5px;display:flex;align-items:center;font-family:"Carlito",Calibri,sans-serif;font-weight:700;font-size:14px;color:#aaa}
.field svg{margin:0 8px 0 12px}
.field .divider{width:1px;height:24px;background:#ccc;margin-right:8px}
.field.user{top:580px}.field.pass{top:627px}.field.repass{top:677px}
.submit-btn{position:absolute;left:688px;top:743px;width:217px;height:46px;border-radius:6px;border:1px solid #5e8a30;background:linear-gradient(#9fd067,#6aa03a);color:#fff;font-weight:700;font-size:19px;letter-spacing:.5px;display:flex;align-items:center;justify-content:center;text-shadow:0 1px 1px rgba(0,0,0,.4)}
.site-footer{position:absolute;top:850px;width:1200px;text-align:center;font-size:12px;line-height:18px;color:var(--text-soft)}
.site-footer .sep{margin:0 18px}
</style>
</head>
<body>
<header class="site-header">
  <div class="brand"><span class="brand-mark"></span><span class="brand-name">Trellis Parcel Market</span></div>
</header>
<section class="hero"></section>
<h1 class="hero-title">Daily Updated Listings Directly From The Source:</h1>
<p class="hero-sub">At vero eos et accusamus et iusto odio dignissimos ducimus qui blanditiis praesentium</p>
<p class="hero-quote">“Corrupti quos dolores et quas molestias dignissimos ducimus qui blanditiis praesentium voluptatum deleniti atque corrupti quos dolores et quas molestias excepturi sint occaecati cupiditate non provident, simiCorrupti quos do-lores et quas molestias dignissimos ducimus qui blanditiis praesentium voluptatum deleniti atque corrupti quos dolores et quas molestias excepturi sint occaecati cupiditate non provident, simi”</p>

<span class="selected-pointer"></span>
<div class="category is-selected" style="left:367px;top:309px;width:110px">
  <span class="thumb" role="img" aria-label="Foreclosure for-sale sign in front of a house" style="width:110px;height:84px;background:linear-gradient(#6f8c5a,#8a3a2e)"></span>Bank-Owned</div>
<div class="category" style="left:493px;top:322px;width:111px">
  <span class="thumb" role="img" aria-label="Crowd at a property auction" style="width:111px;height:86px;background:linear-gradient(#d9a36b,#7a5a3e)"></span>Auctions</div>
<div class="category" style="left:621px;top:322px;width:113px">
  <span class="thumb" role="img" aria-label="House keys handed over between hands" style="width:113px;height:86px;background:linear-gradient(#8aa0b0,#b9876a)"></span>Short Sales</div>
<div class="category" style="left:749px;top:322px;width:110px">
  <span class="thumb" role="img" aria-label="Older two-storey house needing repair" style="width:110px;height:86px;background:linear-gradient(#9cbfd6,#7e8a6a)"></span>Fixer Uppers</div>

<section class="access-panel"></section>
<h2 class="access-title">GET INSTANT <span>Access to:</span></h2>
<svg class="access-arrow" width="52" height="58" viewBox="0 0 52 58" aria-hidden="true">
  <path d="M22 2 C4 12 2 34 26 42 L22 50 L50 50 L36 26 L32 34 C16 30 12 18 22 2 Z" fill="var(--accent-orange)"/>
</svg>
<div class="benefit blue">Over 2 million properties up to 60% below market value.</div>
<div class="benefit orange">Over 2 million properties up to 60% below market value.</div>
<div class="benefit green">Over 2 million properties up to 60% below market value.</div>
<div class="benefit black">Over 2 million properties up to 60% below market value.</div>

<form class="register-box" aria-label="Registration"></form>
<h2 class="register-title">REGISTER NOW <span>TO DETAILS</span></h2>
<p class="register-sub">It's quick, easy and reliable!</p>
<div class="keys-art" role="img" aria-label="Bunch of house keys on a ring"></div>
<label class="field user">
  <svg width="14" height="16" viewBox="0 0 14 16" aria-hidden="true"><circle cx="7" cy="4.5" r="4" fill="#aaa"/><path d="M0 16 C0 9 14 9 14 16Z" fill="#aaa"/></svg>
  <span class="divider"></span>Choose a username:</label>
<label class="field pass">
  <svg width="12" height="16" viewBox="0 0 12 16" aria-hidden="true"><path d="M3 7V4.5a3 3 0 0 1 6 0V7" fill="none" stroke="#aaa" stroke-width="2"/><rect y="7" width="12" height="9" rx="1" fill="#aaa"/></svg>
  <span class="divider"></span>Choose a password:</label>
<label class="field repass">
  <svg width="12" height="16" viewBox="0 0 12 16" aria-hidden="true"><path d="M3 7V4.5a3 3 0 0 1 6 0V7" fill="none" stroke="#aaa" stroke-width="2"/><rect y="7" width="12" height="9" rx="1" fill="#aaa"/></svg>
  <span class="divider"></span>re-type password:</label>
<div class="submit-btn">Submit &amp; Continue</div>

<footer class="site-footer">
  <div>TrellisParcelMarket.com, 2450 Harbor Crest Ave, 210, Bay Point, FL 33999<span class="sep">|</span>FAX: 1-555-014-2290</div>
  <div>Terms and ConditionsPrivacy PolicyCopyright © 1998-2014 TrellisParcelMarket.com Inc., All Rights Reserved.</div>
</footer>
</body>
</html>
```